Business Card Design Project

I need the following:

Logo -
Name - Dale Prewitt
Title - Customer Experience Officer
Web - www.bvrh.net
Phone - 555-417-3068
Updates

Project Deadline Extended
Reason: I launched the project later than anticipated. I look forward to seeing your designs. Dale

Industry/Entity Type

Business

```html
<!DOCTYPE html>
<html lang="en">
<head>
<meta charset="utf-8">
<title>Bluevale Relay Hub – Business Card</title>
<link href="https://fonts.googleapis.com/css2?family=Open+Sans:wght@400;600;700;800&display=swap" rel="stylesheet">
<style>
  :root {
    --page-bg: #e4e5e7;
    --band-light: #8ccde8;
    --card-white: #ffffff;
    --blue-top: #5580ae;
    --blue-bottom: #1b3a6e;
    --brand-blue: #1f64b0;
    --ink: #141414;
    --text-light: #ffffff;
    --link-blue: #1a7fd0;
  }
  * { margin: 0; padding: 0; box-sizing: border-box; }
  html, body {
    width: 1200px; height: 864px; overflow: hidden;
    background: var(--page-bg);
    font-family: "Open Sans", Arial, sans-serif;
  }
  .card {
    position: absolute; left: 100px; top: 146px;
    width: 1000px; height: 572px;
    background: var(--card-white);
    box-shadow: 0 10px 30px rgba(0,0,0,0.18);
    overflow: hidden;
  }
  .card__top-band {
    position: absolute; left: 0; top: 0; width: 100%; height: 46px;
    background: var(--band-light);
  }
  .card__lower {
    position: absolute; left: 0; top: 250px; width: 100%; height: 322px;
    background: linear-gradient(180deg, var(--blue-top), var(--blue-bottom));
  }
  .brand {
    position: absolute; left: 250px; top: 70px;
    display: flex; align-items: center; gap: 28px;
  }
  .brand__dot {
    width: 150px; height: 150px; border-radius: 50%;
    background: var(--brand-blue);
  }
  .brand__text { display: flex; flex-direction: column; }
  .brand__name {
    font-weight: 800; font-size: 34px; line-height: 36px;
    letter-spacing: 1px; color: var(--ink); text-transform: uppercase;
  }
  .brand__web {
    display: flex; align-items: center; gap: 8px; margin-top: 6px;
    font-weight: 700; font-size: 15px; color: var(--link-blue);
  }
  .brand__rule { flex: 1; height: 2px; background: var(--link-blue); }
  .person {
    position: absolute; left: 180px; top: 440px; color: var(--text-light);
  }
  .person__name { font-weight: 700; font-size: 30px; letter-spacing: 0.5px; }
  .person__title { font-size: 17px; font-weight: 600; margin-top: 2px; }
  .contact {
    position: absolute; left: 560px; top: 290px; list-style: none;
    color: var(--text-light); font-size: 21px;
  }
  .contact__item {
    display: flex; align-items: flex-start; gap: 18px; margin-bottom: 8px;
    line-height: 28px;
  }
  .contact__icon { width: 22px; height: 22px; margin-top: 4px; flex: none; }
</style>
</head>
<body>
  <div class="card">
    <div class="card__top-band"></div>
    <div class="brand">
      <div class="brand__dot"></div>
      <div class="brand__text">
        <span class="brand__name">Bluevale<br>Relay Hub</span>
        <span class="brand__web"><span class="brand__rule"></span>www.bvrh.net<span class="brand__rule"></span></span>
      </div>
    </div>
    <div class="card__lower"></div>
    <div class="person">
      <div class="person__name">DALE PREWITT</div>
      <div class="person__title">Customer Experience Officer</div>
    </div>
    <ul class="contact">
      <li class="contact__item">
        <svg class="contact__icon" viewBox="0 0 24 24" fill="#fff"><path d="M2 9c0-3 4-5 10-5s10 2 10 5v2h-5V9c-2-1-8-1-10 0v2H2z"/><rect x="5" y="12" width="14" height="8" rx="1"/></svg>
        <span>555-417-3068</span>
      </li>
      <li class="contact__item">
        <svg class="contact__icon" viewBox="0 0 24 24" fill="none" stroke="#fff" stroke-width="2"><rect x="3" y="4" width="18" height="12"/><path d="M12 16v4M8 20h8"/></svg>
        <span>www.bvrh.net</span>
      </li>
      <li class="contact__item">
        <svg class="contact__icon" viewBox="0 0 24 24" fill="none" stroke="#fff" stroke-width="2"><rect x="3" y="6" width="18" height="12"/><path d="M3 6l9 7 9-7"/></svg>
        <span>info@bvrh.net</span>
      </li>
      <li class="contact__item">
        <svg class="contact__icon" viewBox="0 0 24 24" fill="#fff"><path d="M12 3l10 9h-3v9h-5v-6h-4v6H5v-9H2z"/></svg>
        <span>Lantern Advisory Inc 00<br>Ave Brookfield, NJ 00000</span>
      </li>
    </ul>
  </div>
</body>
</html>
```